Web Design Project for Communications Agency

The design I need (PSD file) is for an agency offering specialised PR and communications services for customers in the healthcare sector.

OBJECTIVES OF THE WEBSITE:
1. To promote the agency's communication services
2. To position Solène Verbruggen as an industry leader, an expert in healthcare PR and communications by highlighting blogposts and social media.

WHAT I NEED:
1st, I need the design for the Home Page ONLY.
Once approved, I will need the other pages designed as well. (Here is prototype that we've already developed for the Website that will guide you in the design:
http://qoravenlab.com/solenverbruggen/)

VISUAL INSPIRATION
We want to give this Website a "Flat Design" look. Here are some websites for inspiration :
- http://lumbrafolk.com/#!/process
- http://www.quillmarsh.co/
- http://dorvellink.com/

Also, reuse images found on the company's current Website :
http://www.solenverbruggen.com/fr/index.html

HOMEPAGE MAIN ELEMENTS:
1. Main menu : 6 sections
Accueil | Agence | Services | Approche | Publications | Contact

2. Main Call To Action (big dark rectangle in prototype):
Can be slider or just an information bloc.

3. Publications récentes :
The 4 latest blog posts must be features on the homepage (will be linked with the "Publications" section)

4. Dynamic Footer :
Contains a Pépieur feed and a Subscribe to our Newsletter feature (revecez nos publications)

OTHER PAGES (to design once Homepage is approved)
- Agence (about us)
- Services (our team)
- Approche (our approach)
- Publications (blog articles)
- Contact (Contact us)

• Please refer to prototype :
http://qoravenlab.com/solenverbruggen/
Must have ALL features present in prototype.

Also, must reuse this picture in the design : http://solenverbruggen.com/static/images/home-big-box.jpg

Finally, you will find attached the company logo.

```html
<!DOCTYPE html>
<html lang="fr">
<head>
<meta charset="utf-8">
<title>Solène Verbruggen — Gestion d'enjeux, affaires publiques</title>
<link href="https://fonts.googleapis.com/css2?family=Arimo:wght@400;700&display=swap" rel="stylesheet">
<style>
:root{
  --red:#c8283a;
  --red-dark:#a8172a;
  --ink:#111;
  --band:#e4e4e4;
  --hero:#ebebeb;
  --footer:#343434;
  --white:#fff;
}
*{box-sizing:border-box;margin:0;padding:0}
html,body{width:1017px;height:1200px;overflow:hidden;background:var(--white)}
body{font-family:"Arimo",Arial,sans-serif;color:var(--ink)}
.stage{position:relative;width:1000px;height:1180px;transform:scale(1.017);transform-origin:0 0}
.abs{position:absolute}
a{color:inherit}

/* header */
.brand{left:138px;top:30px;z-index:2}
.brand-name{color:var(--red);font-size:30px;line-height:32px;font-weight:400;letter-spacing:-.5px}
.brand-tag{left:140px;top:128px;z-index:2;font-size:10.5px;font-weight:700;color:#333;line-height:13px;letter-spacing:.3px}
.brand-tag span{display:block;color:#888}
.lang{left:668px;top:87px;font-size:14px;text-decoration:underline}
.social{top:83px;width:24px;height:24px;border-radius:50%;background:var(--red)}
.nav-band{left:0;top:123px;width:1000px;height:40px;background:var(--band);border-top:1px solid var(--red);border-bottom:1px solid var(--red)}
.nav{top:135px;font-size:14.5px;font-weight:700;text-decoration:none}

/* hero */
.hero{left:0;top:163px;width:1000px;height:331px;background:var(--hero);box-shadow:0 6px 14px -6px rgba(0,0,0,.35)}
.hero-cube{left:95px;top:205px;width:250px;height:240px;background:radial-gradient(circle at 55% 40%,#fafafa 0,#e2e2e2 60%,#ebebeb 75%);border-radius:4px}
.hero-copy{left:373px;top:241px;z-index:2;font-size:21px;line-height:22px;color:#111}
.btn{display:flex;align-items:center;color:var(--white);text-decoration:none;white-space:nowrap;background:linear-gradient(#d23a4b,#b21f31);border-radius:22px;box-shadow:0 3px 5px rgba(0,0,0,.3)}
.hero-btn{left:376px;top:349px;width:176px;height:43px;font-size:18px;padding-left:19px}
.hero-btn .arrow{position:absolute;right:8px;top:8px;width:27px;height:27px;border-radius:50%;background:#8c1423}
.hero-portrait{left:655px;top:200px;width:287px;height:294px;background:linear-gradient(#6a4030 0,#b98a72 45%,#d8c2ac 100%);border-radius:140px 140px 0 0}

/* publications */
.section-title{left:140px;top:532px;font-size:21px;font-weight:700;color:var(--red-dark)}
.card{top:570px;width:234px;height:273px;border:1px solid var(--red);background:var(--white);box-shadow:0 10px 10px -8px rgba(0,0,0,.2)}
.card-media{position:absolute;left:10px;top:9px;width:213px;height:141px;border:1px solid #777}
.card-title{position:absolute;left:19px;top:157px;font-size:11px;font-weight:700}
.card-date{position:absolute;left:19px;top:168px;font-size:11px}
.card-text{position:absolute;left:19px;top:190px;width:190px;font-size:11px;line-height:11px}
.card-link{position:absolute;right:19px;top:244px;font-size:11px;color:var(--red);text-decoration:underline}
.carousel-arrow{top:692px;width:28px;height:28px;border-radius:50%;background:var(--red-dark)}

/* footer */
.footer{left:0;top:918px;width:1000px;height:262px;background:radial-gradient(ellipse at 50% 0,#4a4a4a 0,var(--footer) 55%);border-top:2px solid var(--red)}
.feed-name{left:150px;top:950px;font-size:34px;font-weight:700;color:#5cc4ee}
.tweets{left:152px;top:1009px;width:210px;font-size:9px;line-height:10px;color:var(--white)}
.tweets p{margin-bottom:5px}
.tweets em{font-style:normal;color:var(--red)}
.footer-btn{height:31px;font-size:14px;justify-content:center}
.follow{left:147px;top:1112px;width:180px;font-size:12.5px}
.news-title{left:471px;top:970px;font-size:18px;font-weight:700;line-height:19px;color:var(--white)}
.field{left:409px;width:209px;height:23px;background:var(--white);font-size:13px;color:#444;padding:3px 9px}
.subscribe{left:405px;top:1112px;width:173px;justify-content:flex-start;padding-left:33px}
.contact-line{left:718px;font-size:14px;line-height:14px;color:var(--white)}
.copyright{left:698px;top:1126px;font-size:10.5px;color:var(--red)}
</style>
</head>
<body>
<div class="stage">

  <header>
    <div class="abs brand"><div class="brand-name">solène<br>verbruggen</div></div>
    <a class="abs lang" href="#">English</a>
    <span class="abs social" style="left:733px"></span>
    <span class="abs social" style="left:770px"></span>
    <span class="abs social" style="left:808px"></span>
    <span class="abs social" style="left:846px"></span>
    <div class="abs nav-band"></div>
    <div class="abs brand-tag">GESTION D'ENJEUX<span>AFFAIRES PUBLIQUES</span></div>
    <nav>
      <a class="abs nav" style="left:419px" href="#">Accueil</a>
      <a class="abs nav" style="left:487px" href="#">Agence</a>
      <a class="abs nav" style="left:557px" href="#">Services</a>
      <a class="abs nav" style="left:630px" href="#">Approche</a>
      <a class="abs nav" style="left:715px" href="#">Publications</a>
      <a class="abs nav" style="left:818px" href="#">Contact</a>
    </nav>
  </header>

  <section>
    <div class="abs hero"></div>
    <div class="abs hero-cube" role="img" aria-label="Cube blanc en 3D avec une croix rouge sur le dessus"></div>
    <div class="abs hero-portrait" role="img" aria-label="Portrait de Solène Verbruggen"></div>
    <p class="abs hero-copy">Cabinet-conseil en<br>communications et affaires<br>publiques spécialisé dans<br>le secteur de la santé.</p>
    <a class="abs btn hero-btn" href="#">En savoir plus
      <span class="arrow"><svg width="27" height="27" viewBox="0 0 27 27"><path d="M7 12h8V8l6 5.5-6 5.5v-4H7z" fill="#fff"/></svg></span>
    </a>
  </section>

  <section>
    <h2 class="abs section-title">Publication récentes</h2>
    <span class="abs carousel-arrow" style="left:99px"><svg width="28" height="28"><path d="M17 8v12l-8-6z" fill="#fff"/></svg></span>
    <span class="abs carousel-arrow" style="left:884px"><svg width="28" height="28"><path d="M11 8v12l8-6z" fill="#fff"/></svg></span>

    <article class="abs card" style="left:138px">
      <div class="card-media" role="img" aria-label="Capsules de médicaments posées sur une ordonnance" style="background:linear-gradient(135deg,#d8e4ee,#f2f2f2 50%,#c9c9c9)"></div>
      <h3 class="card-title">Titre de la publication</h3>
      <p class="card-date">23 juillet 2013</p>
      <p class="card-text">Velit esse cillum dolore eu fugiat nulla pariatur. Excepteur sint occaecat cupidatat non proident, sunt in culpa qui officia deserunt mollit anim id est laborum.</p>
      <a class="card-link" href="#">Article complet &nbsp;&gt;</a>
    </article>
    <article class="abs card" style="left:388px">
      <div class="card-media" role="img" aria-label="Équipe de secours sous une tente médicale" style="background:linear-gradient(#e9e3e0,#9a8a80 60%,#5a5350)"></div>
      <h3 class="card-title">Titre de la publication</h3>
      <p class="card-date">23 juillet 2013</p>
      <p class="card-text">Velit esse cillum dolore eu fugiat nulla pariatur. Excepteur sint occaecat cupidatat non proident, sunt in culpa qui officia deserunt mollit anim id est laborum.</p>
      <a class="card-link" href="#">Article complet &nbsp;&gt;</a>
    </article>
    <article class="abs card" style="left:638px">
      <div class="card-media" role="img" aria-label="Flacons de pilules orange tenus par un médecin" style="background:linear-gradient(90deg,#f0f0f0,#f3a93a 40%,#e8e8e8)"></div>
      <h3 class="card-title">Titre de la publication</h3>
      <p class="card-date">23 juillet 2013</p>
      <p class="card-text">Velit esse cillum dolore eu fugiat nulla pariatur. Excepteur sint occaecat cupidatat non proident, sunt in culpa qui officia deserunt mollit anim id est laborum.</p>
      <a class="card-link" href="#">Article complet &nbsp;&gt;</a>
    </article>
  </section>

  <footer>
    <div class="abs footer"></div>

    <div class="abs feed-name">Pépieur</div>
    <div class="abs tweets">
      <p>Velit esse cillum dolore eu fugiat nulla pariatur. Excepteur sint occaecat cupidatat non proident. <em>@SoleneVerbruggen #EnjeuSanté</em></p>
      <p>Velit esse eu fugiat nulla pariatur. Excepteur sint occaecat cupidatat non proident. <em>@SoleneVerbruggen #EnjeuSanté</em></p>
      <p>Velit esse cillum dolore eu fugiat nulla pariatur. Excepteur sint occaecat cupidatat non proident <em>@SoleneVerbruggen #EnjeuSanté</em></p>
    </div>
    <a class="abs btn footer-btn follow" href="#">Suivre @SoleneVerbruggen</a>

    <svg class="abs" style="left:409px;top:958px" width="52" height="52" viewBox="0 0 52 52">
      <path d="M3 2h22l10 10v36H3z" fill="none" stroke="#fff" stroke-width="3"/>
      <path d="M10 16h16M10 23h16M10 30h10" stroke="#fff" stroke-width="3"/>
      <circle cx="38" cy="38" r="11" fill="#343434" stroke="#fff" stroke-width="3"/>
      <path d="M38 32v10M33 38l5 5 5-5" fill="none" stroke="#fff" stroke-width="3"/>
    </svg>
    <h3 class="abs news-title">Revecez nos<br>publications</h3>
    <div class="abs field" style="top:1024px">Votre nom</div>
    <div class="abs field" style="top:1061px">Votre courriel</div>
    <a class="abs btn footer-btn subscribe" href="#">Abonnez-vous
      <svg style="position:absolute;right:10px;top:7px" width="18" height="18" viewBox="0 0 18 18"><path d="M1 8L17 1 12 17 8 10z M8 10L17 1" fill="none" stroke="#fff" stroke-width="1.5"/></svg>
    </a>

    <svg class="abs" style="left:687px;top:982px" width="20" height="20" viewBox="0 0 20 20"><rect x="1" y="1" width="18" height="18" fill="none" stroke="#fff" stroke-width="2"/><path d="M6 5v10M14 5v10M6 10h8" stroke="#fff" stroke-width="2"/></svg>
    <p class="abs contact-line" style="top:981px">142, rue des Martinets<br>Saint-Lambertin<br>Québec&nbsp; J3X 4B7</p>
    <svg class="abs" style="left:687px;top:1036px" width="14" height="18" viewBox="0 0 14 18"><rect x="2" y="1" width="10" height="16" rx="1" fill="none" stroke="#fff" stroke-width="2"/><path d="M5 6h4M5 9h4M5 12h4" stroke="#fff"/></svg>
    <p class="abs contact-line" style="top:1038px">450.555.0187</p>
    <svg class="abs" style="left:687px;top:1066px" width="18" height="13" viewBox="0 0 18 13"><rect x="1" y="1" width="16" height="11" fill="none" stroke="#fff" stroke-width="1.5"/><path d="M1 1l8 6 8-6M1 12l6-5M17 12l-6-5" fill="none" stroke="#fff" stroke-width="1.5"/></svg>
    <a class="abs contact-line" style="top:1066px;text-decoration:underline" href="#">info@solenverbruggen.com</a>
    <p class="abs copyright">Copyright 2013. SOLÈNE VERBRUGGEN</p>
  </footer>

</div>
</body>
</html>
```